Coin collector banner ad for specialty insurance

We need a logo designed banner ad (multiple ads) to align with the coin collector market while incorporating color palette logo and call to action. Color palette of Fernholt. Dimension, images, example designs and color palette attached. The context should include 'Specialty Insurance for your coin collection' please refer to the designed examples

Target Market(s)

Coin collectors 30-65+ years of age primarily male

Industry/Entity Type

Insurance

Font styles to use
Sans Serif

Requirements
Must have
• color palette, logo, word mark, Call to Action, The words 'Specialty Insurance for your coin collection'
Nice to have
• Call to actions
Should not have
• ba

```html
<!DOCTYPE html>
<html lang="en">
<head>
<meta charset="utf-8">
<title>Fernholt Insurance – Specialty Insurance for Your Coin Collection</title>
<link rel="stylesheet" href="https://fonts.googleapis.com/css2?family=Jost:wght@400;500;600&family=Saira+Extra+Condensed:wght@700&family=Josefin+Sans:wght@400;600&display=swap">
<style>
  :root {
    --white: #ffffff;
    --ink: #1c1d22;
    --blue-deep: #0a4fb3;
    --blue-mid: #1276d6;
    --blue-bright: #1ca6e6;
    --blue-sky: #4cc0f0;
    --gold-light: #f3d27a;
    --gold: #d9a93d;
    --gold-dark: #a8771f;
  }
  * { margin: 0; padding: 0; box-sizing: border-box; }
  html, body { width: 1200px; height: 628px; overflow: hidden; background: var(--white); }
  .banner {
    position: relative;
    width: 1200px;
    height: 628px;
    overflow: hidden;
    background: var(--white);
    font-family: "Jost", sans-serif;
  }
  .backdrop { position: absolute; inset: 0; }
  .coin-visual {
    position: absolute;
    left: 62px;
    top: 44px;
    width: 462px;
    height: 462px;
    border-radius: 50%;
    background: radial-gradient(circle at 40% 35%, var(--gold-light) 0%, var(--gold) 55%, var(--gold-dark) 100%);
    box-shadow: 0 6px 18px rgba(0, 30, 80, 0.35);
  }
  .brand {
    position: absolute;
    top: 40px;
    left: 822px;
    display: flex;
    align-items: center;
    gap: 20px;
  }
  .brand-text { text-align: center; color: var(--ink); }
  .brand-name {
    font-weight: 500;
    font-size: 32px;
    letter-spacing: 1px;
    line-height: 1;
  }
  .brand-tag {
    font-weight: 400;
    font-size: 14px;
    letter-spacing: 7px;
    margin-top: 6px;
    padding-left: 6px;
  }
  .brand-square {
    width: 85px;
    height: 85px;
    background: var(--blue-bright);
  }
  .headline {
    position: absolute;
    right: 82px;
    top: 160px;
    text-align: right;
    font-family: "Saira Extra Condensed", sans-serif;
    font-weight: 700;
    font-size: 84px;
    line-height: 70px;
    letter-spacing: 6px;
    color: var(--blue-mid);
  }
  .headline span { display: block; }
  .subline {
    position: absolute;
    right: 82px;
    top: 318px;
    font-family: "Josefin Sans", sans-serif;
    font-weight: 400;
    font-size: 30px;
    letter-spacing: 3px;
    color: var(--ink);
  }
  .cta {
    position: absolute;
    left: 735px;
    top: 450px;
    width: 465px;
    height: 72px;
    background: var(--blue-bright);
    display: flex;
    align-items: center;
    padding-left: 34px;
    color: var(--white);
    font-family: "Josefin Sans", sans-serif;
    font-size: 38px;
    letter-spacing: 3px;
    text-decoration: none;
  }
  .cta-label { padding-top: 6px; }
  .cta-label strong { font-weight: 600; }
  .cta-icon { position: absolute; left: 334px; top: 12px; }
  .site-url {
    position: absolute;
    left: 92px;
    top: 556px;
    font-family: "Jost", sans-serif;
    font-weight: 400;
    font-size: 24px;
    letter-spacing: 2.5px;
    color: var(--white);
  }
</style>
</head>
<body>
<main class="banner">
  <svg class="backdrop" width="1200" height="628" viewBox="0 0 1200 628" aria-hidden="true">
    <defs>
      <linearGradient id="leftWedge" x1="0" y1="0" x2="0.6" y2="1">
        <stop offset="0" stop-color="#1a8fe3"/>
        <stop offset="1" stop-color="#0a4fb3"/>
      </linearGradient>
      <linearGradient id="cornerBand" x1="0" y1="1" x2="1" y2="0">
        <stop offset="0" stop-color="#0a3f9e"/>
        <stop offset="1" stop-color="#1466cc"/>
      </linearGradient>
    </defs>
    <polygon points="0,40 110,40 600,628 0,628" fill="url(#leftWedge)"/>
    <polygon points="0,40 110,40 330,300 0,150" fill="#2ba9ec" opacity="0.75"/>
    <polygon points="0,380 260,628 0,628" fill="#0a3f9e" opacity="0.6"/>
    <polygon points="560,628 1200,400 1200,628" fill="url(#cornerBand)"/>
    <polygon points="640,628 1200,430 1200,470 760,628" fill="#1c8fe0" opacity="0.6"/>
  </svg>

  <div class="coin-visual" role="img" aria-label="Photograph of a gold 1904 twenty-dollar coin"></div>

  <div class="brand">
    <div class="brand-text">
      <div class="brand-name">FERNHOLT</div>
      <div class="brand-tag">INSURANCE</div>
    </div>
    <div class="brand-square"></div>
  </div>

  <h1 class="headline"><span>SPECIALTY</span><span>INSURANCE</span></h1>
  <p class="subline">FOR YOUR COIN COLLECTION</p>

  <a class="cta" href="#">
    <span class="cta-label">LEARN <strong>MORE</strong></span>
    <svg class="cta-icon" width="48" height="48" viewBox="0 0 48 48" aria-hidden="true">
      <circle cx="24" cy="24" r="22" fill="none" stroke="#ffffff" stroke-width="2.5"/>
      <polygon points="19,14 34,24 19,34" fill="#ffffff"/>
    </svg>
  </a>

  <p class="site-url">WWW.FERNHOLT-INS.COM</p>
</main>
</body>
</html>
```